Task Description:
I’m wanting a professionally designed 8 ½' x 11, 3 fold brochure, both sides, to print as my target audience are those people who primarily don’t have access to the internet. These items will be dropped off in the mailboxes of all households in the city.
However I do have a web site www.civicharborvote.ca where I would like to have it as a document that can be down loaded.
This is my first foray into political office and my message needs to be clear, concise and easy to understand. The brochure should be a bit conservative yet be warm and inviting. I’ve selected two pictures that I think make sense under their respective headings, but I'm open to suggestions.I need to update my picture for the front cover.
There is the possibility of having T shirts and business cards made up, which would be in essence a simpler version of the brochure so please keep this in mind. I ask that you work with me and I will compensate you accordingly for the extras should they be required. You may want to consider making the Civic Harbor Vote into a logo as we own all the web extensions and have applied for copyright protection for branding purposes.
You may want to look at QL Brightmoor http://www.qlbrightmoor.ca/ , or the Silver Pine Trust of Canada www.silverpinetrust.com as two recognizable colour schemes here in Canada but don’t let that limit your imagination.
The content in the flier should remain intact although I am open to some minor suggestions. As you can see my talents as a graphic artist are limited hence my need for that professional make over that will give it a bit of razzle dazzle and set me out from the other candidates. So use your imagination!!
Target Market(s)
Middle age voters who may or may not have access to the internet and still prefer print
Industry/Entity Type
Conservative
Look and feel

```html
<!DOCTYPE html>
<html lang="en">
<head>
<meta charset="utf-8">
<title>Civic Harbor Vote – Brochure Inside</title>
<link href="https://fonts.googleapis.com/css2?family=Arimo:ital,wght@0,400;0,700;1,400;1,700&display=swap" rel="stylesheet">
<style>
  :root{
    --blue:#0f5aa8;
    --text-blue:#1f5ba6;
    --green:#5aa51e;
    --light-green:#b7d99a;
    --pale:#eef1ee;
    --fade-blue:#9bb5d6;
    --white:#ffffff;
  }
  *{box-sizing:border-box;margin:0;padding:0}
  html,body{width:1200px;height:933px;overflow:hidden;background:var(--white)}
  body{font-family:"Arimo",Arial,sans-serif;color:var(--text-blue);position:relative}
  .brochure{position:absolute;inset:0;width:1200px;height:933px}
  .top-band{position:absolute;left:0;top:0;width:1200px;height:27px;background:var(--green)}
  .bottom-band{position:absolute;left:0;top:901px;width:1200px;height:32px;background:var(--green)}
  .site{position:absolute;top:7px;color:var(--white);font-weight:700;font-size:16px;letter-spacing:4.6px}
  .site.left{left:44px}
  .site.right{left:862px}

  .panel{position:absolute;top:27px;height:874px;width:400px}
  .panel.economy{left:0}
  .panel.opportunities{left:404px;width:392px;background:var(--pale)}
  .panel.safety{left:796px;width:404px}

  .panel-head{height:102px;display:flex;align-items:center;justify-content:center;font-size:32px}
  .economy .panel-head,.safety .panel-head{background:var(--blue);color:var(--white)}
  .opportunities .panel-head{color:var(--green);font-size:33px;padding-top:6px}

  .lead{font-style:italic;color:var(--green);font-size:16.5px;line-height:21.5px}
  .lead .cap{font-weight:700;font-size:27px;line-height:1}
  .lead.blue{color:var(--text-blue)}
  .lead.blue .cap{color:var(--text-blue)}

  .body-text{font-size:16.5px;line-height:21.5px}
  .hl-blue{font-weight:700;color:var(--blue)}
  .hl-green{font-weight:700;color:var(--green)}

  /* economy */
  .economy .lead{position:absolute;left:24px;top:140px;width:360px;text-indent:0}
  .economy .lead span.rest{padding-left:0}
  .points{position:absolute;left:24px;top:229px;width:370px;list-style:none}
  .points li{position:relative;padding-left:20px;margin-bottom:22px}
  .points li::before{content:"";position:absolute;left:2px;top:8px;width:6px;height:6px;border-radius:50%;background:var(--green)}
  .growth-arrow{position:absolute;left:53px;top:700px}
  .vertical{position:absolute;transform:rotate(-90deg);transform-origin:left top;white-space:nowrap;font-size:24px;letter-spacing:14px}
  .growth-word{left:30px;top:874px;color:var(--light-green)}
  .question{position:absolute;left:184px;top:727px;font-style:italic;font-size:16.5px}

  /* opportunities */
  .visual-grass{position:absolute;left:0;top:102px;width:392px;height:144px;background:linear-gradient(135deg,#6ab42a,#4f981a)}
  .sub-head{position:absolute;left:56px;top:283px;font-size:32px;color:var(--green)}
  .opportunities .lead{position:absolute;left:16px;top:340px;width:370px}
  .opp-copy{position:absolute;left:37px;top:430px;width:345px}
  .opp-copy p{margin-bottom:21px}
  .new-word{left:12px;top:866px;color:var(--green);font-size:22px;letter-spacing:8px}

  /* safety */
  .safety .lead{position:absolute;left:33px;top:138px;width:350px}
  .safe-copy{position:absolute;left:56px;top:228px;width:340px}
  .safe-copy p{margin-bottom:21px}
  .community-word{left:20px;top:505px;color:var(--fade-blue);font-size:22px;letter-spacing:10px}
  .family-block{position:absolute;left:0;top:520px;width:404px;height:354px;background:var(--blue)}
  .family-photo{position:absolute;left:41px;top:41px;width:303px;height:239px;background:linear-gradient(160deg,#8a8f97,#3d3a36 60%,#2a2724)}
  .caption{position:absolute;left:0;top:293px;width:404px;text-align:center;color:var(--white);font-size:15.5px}
</style>
</head>
<body>
<div class="brochure">
  <div class="top-band"></div>

  <section class="panel economy">
    <h2 class="panel-head">A Strong Economy</h2>
    <p class="lead"><span class="cap">W</span>ithout a strong economy we can’t afford<br>&nbsp;&nbsp;&nbsp;to pay for social services that we now take<br>&nbsp;&nbsp;&nbsp;for granted.</p>
    <ul class="points body-text">
      <li>Although the City is the largest corporation it is unique in the fact that it revenue stream is tied directly to taxation</li>
      <li>Without new business and new citizens the burden of taxes will fall increasingly on residential taxpayers.</li>
      <li>Our demographics have changed over the years and those changes need to be reflected in the way we tax our citizens.</li>
      <li>Our levels of debts and our future commitments need to be effectively communicated to the people that own this city. You the tax payer!!</li>
      <li>Currently our debt is 178 million dollars with further commitments of 153 million for homes for the aged and the possibility of 100 million dollar multi purpose facility.</li>
    </ul>
    <div class="vertical growth-word">growth</div>
    <svg class="growth-arrow" width="96" height="174" viewBox="0 0 96 174" aria-hidden="true">
      <polygon points="48,0 96,74 60,74 60,174 36,174 36,74 0,74" fill="var(--green)"/>
    </svg>
    <p class="question">How will we pay for this?</p>
  </section>

  <section class="panel opportunities">
    <h2 class="panel-head">New Opportunities</h2>
    <div class="visual-grass" role="img" aria-label="Stylised white grass blades on a green square"></div>
    <h3 class="sub-head">New Beginnings</h3>
    <p class="lead blue"><span class="cap">A</span>s a city we need to rekindle that passion<br>&nbsp;&nbsp;&nbsp;that made us the most modern small city<br>&nbsp;&nbsp;&nbsp;in North America at the turn of the century.</p>
    <div class="opp-copy body-text">
      <p>That means, if you currently own and operate a business large or small <span class="hl-blue">we need your input</span> to improve the efficiency of how we deliver services. No more endless meetings without any results.</p>
      <p>If you’re in the planning stages and need assistance, the city will be there to offer <span class="hl-green">support and guidance</span>.</p>
      <p><span class="hl-green">Regional projects</span> are vitality important to the flow of goods and services.</p>
      <p><span class="hl-green">As a Civic Harbor Vote</span> I have personally spoken to the CEO’s of several new industries that have never even considered Harbor Bay before they received my call. These are leading edge technologies that have the high growth potential. Jobs and opportunities for young and old alike.</p>
    </div>
    <div class="vertical new-word">new</div>
  </section>

  <section class="panel safety">
    <h2 class="panel-head">A Safe Community</h2>
    <p class="lead"><span class="cap">W</span>ithout a safe community it will be difficult<br>&nbsp;&nbsp;&nbsp;to attract new people and new businesses<br>&nbsp;&nbsp;&nbsp;to our community.</p>
    <div class="vertical community-word">community</div>
    <div class="safe-copy body-text">
      <p><span class="hl-blue">I have a plan</span> that will utilize the resources of the current police force to better facilitate the services that are currently provided.</p>
      <p><span class="hl-blue">Incentive programs</span> need to be initiated in all city departments at the ground level so that good ideas don’t get lost in bureaucracy.</p>
      <p><span class="hl-blue">Seniors and youth</span> are the most vulnerable of all. I have plan that will identify those groups and make sure that those people receive the benefits that they deserve.</p>
    </div>
    <div class="family-block">
      <div class="family-photo" role="img" aria-label="Photo of the candidate's father seated in an arena beside a team mascot"></div>
      <p class="caption">My Dad @ 92 with HCU Mascot</p>
    </div>
  </section>

  <div class="bottom-band">
    <span class="site left">www.civicharborvote.ca</span>
    <span class="site right">www.civicharborvote.ca</span>
  </div>
</div>
</body>
</html>
```